Tree Pruning Website

We need a website for a tree Arborist, pruning company called Hollow Ridge Branchworks. We look after all types of trees, knock down trees and prune trees. Our target market is from domestic clients to government clients and everything in between.

We would like to see the use of our main colours which are orange and green

We are not looking forward in seeing a template that we have seen before but a unique template. We have designed 5 templates ourselves and we wish for the design community to take our designs to the next level.

We have also designed a template for things that **we are not** looking for (Version 4)

To make it fair for everyone, we are also not giving out any participation payments as we have had. One winner will take all of the payment!!!

I Have attached a image of the designs and a image of a tree.

We are just looking at the PSD file been developed. We have our own team who can slice the image up into a HTML format.

Target Market(s)

Everyone who needs to cut down a tree

Industry/Entity Type

Government

Requirements
Must have
• Logo on front page
A List of our services
jQuery slider on page
Phone Number on every page

```html
<!DOCTYPE html>
<html lang="en">
<head>
<meta charset="utf-8">
<title>Hollow Ridge Branchworks</title>
<link rel="stylesheet" href="https://fonts.googleapis.com/css2?family=Josefin+Sans:wght@400;600;700&family=Open+Sans:ital,wght@0,400;0,600;0,700;1,400&display=swap">
<style>
:root{
  --orange:#f7941d;
  --orange-deep:#e98a12;
  --orange-text:#f39a1f;
  --green-dark:#1f2a12;
  --green-mid:#4f6a26;
  --green-light:#9bbd45;
  --leaf:#a8cc1c;
  --ink:#555555;
  --ink-strong:#333333;
  --white:#ffffff;
  --paper:#f2f2f2;
  --footer:#3b3b3b;
  --footer-base:#2f2f2f;
}
*{margin:0;padding:0;box-sizing:border-box}
html,body{width:1200px;height:1000px;overflow:hidden}
body{position:relative;font-family:"Open Sans",sans-serif;background:var(--white);color:var(--ink)}
.abs{position:absolute}

/* hero */
.hero{left:0;top:0;width:1200px;height:385px;
  background:
    radial-gradient(ellipse 260px 160px at 620px 120px,rgba(168,190,90,.55),transparent 70%),
    radial-gradient(ellipse 300px 200px at 1080px 200px,rgba(160,185,80,.6),transparent 70%),
    radial-gradient(ellipse 260px 180px at 150px 170px,rgba(130,160,70,.55),transparent 70%),
    radial-gradient(ellipse 200px 140px at 380px 330px,rgba(110,140,55,.5),transparent 70%),
    linear-gradient(180deg,#3a4a1e 0%,#56692a 45%,#2c3616 100%);}
.hero-shade{left:0;top:0;width:1200px;height:385px;
  background:linear-gradient(90deg,rgba(20,25,10,.15) 0%,rgba(20,25,10,.05) 50%,rgba(10,12,5,.45) 78%,rgba(20,25,10,.1) 100%)}
.topbar{left:0;top:0;width:1200px;height:75px;background:rgba(10,12,8,.82)}
.brand{left:212px;top:17px;display:flex;align-items:center;gap:10px;color:var(--white);
  font-family:"Open Sans",sans-serif;font-weight:600;font-size:15px;line-height:17px;letter-spacing:.5px;text-transform:uppercase}
.brand-dot{width:12px;height:12px;border-radius:50%;background:var(--white)}
.nav{left:449px;top:32px;display:flex;gap:15px;font-family:"Josefin Sans",sans-serif;font-weight:600;font-size:11.5px;color:var(--white);letter-spacing:.3px}
.nav a{color:inherit;text-decoration:none;padding-bottom:4px}
.nav a.current{border-bottom:2px solid var(--white)}
.actions{left:816px;top:27px;width:177px;height:25px;display:flex;border:1px solid #8a5a14;border-radius:2px}
.actions a{flex:1;display:flex;align-items:center;justify-content:center;font-family:"Josefin Sans",sans-serif;font-weight:600;font-size:11.5px;color:var(--orange-text);text-decoration:none;padding-top:2px}
.actions a+a{border-left:1px solid #8a5a14}
.intro{left:212px;top:207px;width:380px;font-size:12.6px;line-height:18px;color:var(--white)}
.callout{left:817px;top:204px;font-size:13.8px;font-weight:700;line-height:17px;color:var(--white)}
.phone-box{left:805px;top:245px;width:219px;height:40px;background:rgba(170,100,20,.6);border-radius:2px;display:flex;align-items:center;gap:12px;padding-left:12px;color:var(--white);font-weight:700;font-size:27px}

/* rules */
.rule{left:139px;width:916px;height:4px;background:var(--orange)}

/* services */
.service{width:170px;text-align:center}
.service-icon{width:46px;height:46px;margin:0 auto;border-radius:50%;background:radial-gradient(circle at 50% 40%,var(--leaf),#6d9a1a)}
.service h3{margin-top:20px;font-family:"Josefin Sans",sans-serif;font-weight:600;font-size:12.5px;color:var(--orange-text);letter-spacing:.3px}
.service p{margin-top:10px;font-size:10.4px;line-height:14px;color:var(--ink)}
.service b{color:var(--ink-strong);font-weight:700}
.btn{height:25px;width:177px;border-radius:3px;display:flex;align-items:center;justify-content:space-between;padding:0 12px 0 23px;font-family:"Josefin Sans",sans-serif;font-weight:600;font-size:11px;letter-spacing:.3px;text-decoration:none}
.btn-solid{background:var(--orange);color:var(--white)}
.btn-ghost{background:var(--white);color:#9a9a9a;border:1px solid #cfcfcf}

/* testimonials */
.testimonials{left:0;top:671px;width:1200px;height:201px;
  background:radial-gradient(ellipse 260px 180px at 380px 120px,rgba(225,225,225,.9),transparent 70%),linear-gradient(180deg,#f3f3f3,#ececec)}
.quote{width:365px}
.quote blockquote{font-style:italic;font-size:13.6px;line-height:16.5px;color:#666}
.quote cite{display:block;margin-top:12px;font-style:normal;font-size:7.5px;letter-spacing:.4px;color:#888;text-transform:uppercase;text-align:center;padding-right:30px}

/* footer */
.footer{left:0;top:876px;width:1200px;height:79px;background:var(--footer)}
.footer-brand{left:216px;top:904px;display:flex;align-items:center;gap:8px;color:var(--white);font-weight:600;font-size:11px;line-height:13px;text-transform:uppercase}
.footer-brand .brand-dot{width:9px;height:9px}
.footer-info{left:345px;top:909px;display:flex;gap:23px;font-size:10.8px;color:var(--white);text-transform:uppercase}
.base{left:0;top:955px;width:1200px;height:45px;background:var(--footer-base);display:flex;align-items:center;justify-content:center;font-size:10px;color:#8a8a8a}
</style>
</head>
<body>

<section class="abs hero" role="img" aria-label="Blurred photograph of a leafy tree canopy with dark branches"></section>
<div class="abs hero-shade"></div>

<header class="abs topbar"></header>
<div class="abs brand"><span>Hollow Ridge<br>Branchworks</span><span class="brand-dot"></span></div>
<nav class="abs nav">
  <a class="current" href="#">HOME</a>
  <a href="#">ABOUT US</a>
  <a href="#">OUR SERVICES</a>
  <a href="#">OUR WORK</a>
</nav>
<div class="abs actions"><a href="#">GET A QUOTE</a><a href="#">CONTACT US</a></div>

<p class="abs intro">Since 1990 we have been providing the highest quality and most up-to-date tree and shrub treatments available. We have the expertise, personnel and equipment to enhance the health and beauty of your trees and shrubs.</p>
<p class="abs callout">Call us to make arrangements<br>for a free property examination</p>
<div class="abs phone-box">
  <svg width="20" height="20" viewBox="0 0 24 24" aria-hidden="true"><path d="M6.6 10.8c1.4 2.8 3.8 5.1 6.6 6.6l2.2-2.2c.3-.3.7-.4 1-.2 1.1.4 2.3.6 3.6.6.6 0 1 .4 1 1V20c0 .6-.4 1-1 1C10.6 21 3 13.4 3 4c0-.6.4-1 1-1h3.5c.6 0 1 .4 1 1 0 1.3.2 2.5.6 3.6.1.3 0 .7-.2 1L6.6 10.8z" fill="#ffffff"/></svg>
  <span>08-5550-0147</span>
</div>

<div class="abs rule" style="top:385px"></div>

<section>
  <div class="abs service" style="left:193px;top:419px">
    <div class="service-icon" role="img" aria-label="Small tree illustration"></div>
    <h3>DIAGNOSIS</h3>
    <p>These inpsections are made for your safety. <b>Qualified arborists</b> can help you decide if a tree should be removed.</p>
  </div>
  <div class="abs service" style="left:405px;top:419px">
    <div class="service-icon" role="img" aria-label="Young sapling illustration"></div>
    <h3>TREATMENT</h3>
    <p>Trees receiving regular applications of <b>essential nutrients</b> look better and live longer.</p>
  </div>
  <div class="abs service" style="left:618px;top:419px">
    <div class="service-icon" role="img" aria-label="Round canopy tree illustration"></div>
    <h3>TREE PROTECTION</h3>
    <p>These inpsections are made for your safety. Our qualified arborists can <b>help you decide</b> if a tree should be removed.</p>
  </div>
  <div class="abs service" style="left:829px;top:419px">
    <div class="service-icon" role="img" aria-label="Bare tree in a circle illustration"></div>
    <h3>ARBORIST CONSULTS</h3>
    <p>Although <b>tree removal</b> is a last resort, there are circumstances when it is necessary.</p>
  </div>
  <a class="abs btn btn-solid" style="left:827px;top:607px" href="#">OUR SERVICES
    <svg width="14" height="8" viewBox="0 0 14 8" aria-hidden="true"><path d="M0 4h12M9 1l3 3-3 3" stroke="#ffffff" fill="none"/></svg></a>
</section>

<section class="abs testimonials" role="img" aria-label="Faded photograph of a tree-lined avenue"></section>
<div class="abs quote" style="left:198px;top:724px">
  <blockquote>“Felis dolor, faucibus sit amet posuere tincidunt, posuere sit amet lacus. Quisque in quam urna. Mauris nec aliquam ligula. Quisque non massa ipsum, in laoreet ligula.”</blockquote>
  <cite>Joanne P., &nbsp;Client</cite>
</div>
<div class="abs quote" style="left:624px;top:724px">
  <blockquote>“Maecenas non ante sed erat cursus ullamcorper in ut sapien. Nulla tempor tempor arcu cursus mollis. Donec felis dolor, faucibus sit amet posuere tincidunt, posuere sit amet lacus.”</blockquote>
  <cite>Daniel K., &nbsp;Client</cite>
</div>
<a class="abs btn btn-ghost" style="left:827px;top:824px" href="#">OUR WORK
  <svg width="14" height="8" viewBox="0 0 14 8" aria-hidden="true"><path d="M0 4h12M9 1l3 3-3 3" stroke="#aaaaaa" fill="none"/></svg></a>

<div class="abs rule" style="top:872px"></div>

<footer class="abs footer"></footer>
<div class="abs footer-brand"><span>Hollow Ridge<br>Branchworks</span><span class="brand-dot"></span></div>
<div class="abs footer-info">
  <span>48 Kestrel Lane, Ashgrove, WA 6190</span>
  <span>info@hollowridge.com.au</span>
  <span>Phone: 08-5550-0147</span>
  <span>Fax: 08-5550-0182</span>
</div>
<div class="abs base">Copyright 2013, Hollow Ridge</div>

</body>
</html>
```